Dog walking/Pet Sitting company needs a brochure to hook high end apartment tenants

We are looking for a brochure design that we can bring to meetings with high-end apartment and hotel management that will explain who we are, what we do, and how we can help their tenants/guests. I would like it to reflect the same look and feel of our website, carried over to printed brochure. Wesbite is www.harborleashpetcare.com. I can provide the stock images from the website if needed. A bi-fold brochure is ideal, unless you feel the information would fit better on a tri-fold. My company colors are #5D4664 and #5BA046. I would like a more professional tone to it, rather than fun.

Target Market(s)

Demo Professional Females and Males ages 30-50 with pets

Industry/Entity Type

Pet sitting

Font styles to use
Sans Serif

Colors
6b449b
9bcb3c

Requirements
Must have
• the same look and feel as my website; explain who we are, what we do, how we can help; include services offered; Mention that we service Parsippany and surrounding towns. Mention 15 years in business.
Should not have
• do not list pricing on brochure (you can mention pricing is available on the website). No cartoonish feel.

```html
<!DOCTYPE html>
<html lang="en">
<head>
<meta charset="utf-8">
<title>Harbor Leash Pet Care – Bi-fold Brochure</title>
<link href="https://fonts.googleapis.com/css2?family=Open+Sans:ital,wght@0,400;0,600;0,700;0,800;1,400&display=swap" rel="stylesheet">
<style>
:root{
  --purple:#5D4664;
  --green:#4CB763;
  --green-dark:#5BA046;
  --ink:#2b2b2b;
  --paper:#ffffff;
  --backdrop:#ecebe8;
  --rule:#a8805e;
}
*{margin:0;padding:0;box-sizing:border-box}
html,body{width:1200px;height:1137px;overflow:hidden}
body{background:var(--backdrop);font-family:"Open Sans",Arial,sans-serif;color:var(--ink);position:relative}

/* Outer spread */
.outer-spread{position:absolute;left:93px;top:36px;width:1025px;height:514px;box-shadow:0 3px 10px rgba(0,0,0,.25)}
.back-panel{position:absolute;left:0;top:0;width:511px;height:514px;background:var(--purple)}
.cover-panel{position:absolute;left:511px;top:0;width:514px;height:514px;background:var(--green)}
.website-note{position:absolute;left:0;width:511px;top:120px;text-align:center;color:#fff;font-weight:700;font-size:10.5px;line-height:14px}
.website-pill{position:absolute;left:162px;top:173px;width:185px;height:25px;border-radius:7px;background:var(--green);color:#fff;font-weight:700;font-size:10px;line-height:25px;text-align:center}
.brand-mark{position:absolute;left:248px;top:63px;width:120px;height:120px;border-radius:50%;background:#fff;border:2px solid var(--purple);display:flex;align-items:center;justify-content:center;text-align:center}
.brand-name{color:var(--purple);font-weight:700;font-size:15px;line-height:18px}
.photo-strip{position:absolute;left:0;top:251px;width:1025px;height:173px;display:flex}
.photo{height:100%}
.tagline{position:absolute;left:511px;width:514px;top:472px;text-align:center;color:#fff;font-weight:800;font-size:14.5px}

/* Inner spread */
.inner-spread{position:absolute;left:94px;top:580px;width:1029px;height:514px;background:var(--paper);box-shadow:0 3px 10px rgba(0,0,0,.25)}
.fold{position:absolute;left:515px;top:0;width:1px;height:514px;background:var(--rule)}
h2{color:var(--purple);font-weight:800;font-size:19px;position:absolute}
.about-title{left:40px;top:26px}
.about-col{position:absolute;font-size:7.2px;line-height:9px;text-align:justify}
.about-col p{margin-bottom:9px}
.col-left{left:37px;top:58px;width:214px}
.col-right{left:272px;top:60px;width:202px}
.signature{position:absolute;right:555px;top:248px;text-align:right}
.signature-name{font-style:italic;font-size:14px;color:var(--ink)}
.signature-role{font-size:7.2px}
.feature{position:absolute;top:324px;width:150px;text-align:center}
.feature-art{width:64px;height:62px;margin:0 auto;border-radius:6px}
.feature-title{margin-top:26px;color:var(--purple);font-weight:700;font-size:10px;line-height:13px}
.feature-text{margin-top:4px;font-size:7.2px;line-height:9px}
.info-box{position:absolute;left:554px;top:36px;width:222px;height:206px;background:var(--green);color:#fff;font-weight:600;font-size:7.2px;line-height:11px;text-align:justify;padding:24px 22px 0 23px}
.info-photo{position:absolute;left:776px;top:36px;width:205px;height:206px}
.services-title{left:561px;top:276px}
.contact-title{left:781px;top:276px}
.service-list{position:absolute;left:556px;top:307px;list-style:none}
.service-list li{display:table;background:var(--green);color:#fff;font-weight:700;font-size:10px;height:19px;line-height:19px;padding:0 30px 0 10px;border-radius:0 10px 10px 0;margin-bottom:8.6px}
.more{position:absolute;left:686px;top:461px;color:var(--purple);font-weight:700;font-size:10px}
.contact-list{position:absolute;left:785px;top:312px;list-style:none}
.contact-list li{display:flex;align-items:center;height:26px;font-weight:700;font-size:10.5px;color:var(--ink)}
.contact-icon{width:14px;height:14px;margin-right:10px;display:flex;align-items:center;justify-content:center}
.dot{width:10px;height:10px;border-radius:50%;background:var(--purple)}
</style>
</head>
<body>

<section class="outer-spread">
  <div class="back-panel">
    <p class="website-note">Check Our website for<br>pricing and Availability</p>
    <div class="website-pill">www.harborleashpetcare.com</div>
  </div>
  <div class="cover-panel">
    <div class="brand-mark"><span class="brand-name">Harbor<br>Leash</span></div>
  </div>
  <div class="photo-strip">
    <div class="photo" style="width:164px;background:linear-gradient(135deg,#c9b6a0,#6c4a3a)" role="img" aria-label="Woman on a sofa hugging a spaniel"></div>
    <div class="photo" style="width:174px;background:linear-gradient(180deg,#d9cfc2,#8a5a36)" role="img" aria-label="Terrier holding a leather leash in its mouth"></div>
    <div class="photo" style="width:173px;background:linear-gradient(135deg,#b89a84,#e8e2da)" role="img" aria-label="Woman resting her head beside a spaniel"></div>
    <div class="photo" style="width:172px;background:linear-gradient(135deg,#9a7a5a,#e4dcd2)" role="img" aria-label="Woman embracing a shepherd dog"></div>
    <div class="photo" style="width:172px;background:linear-gradient(180deg,#7d7a72,#b09a7a)" role="img" aria-label="Two dogs walking on leashes beside a walker"></div>
    <div class="photo" style="width:170px;background:linear-gradient(135deg,#8c8fa6,#bfae9a)" role="img" aria-label="Tabby cat relaxing in a person's arms"></div>
  </div>
  <p class="tagline">Fully Insured and Bonded Professional Pet Care Specialists</p>
</section>

<section class="inner-spread">
  <h2 class="about-title">About Us</h2>
  <div class="about-col col-left">
    <p>We specialize in one-to-one personalized, quality pet care. We offer many services to cater to your needs. Whether you have dogs, cats, reptiles or rodents, we can help!</p>
    <p>Our business was born out of necessity. There were very few options for pet owners as recently as 15 years ago for pet care when pet owners needed to travel or work long hours. We were in the same boat, with a new puppy and both “mom and dad” working in an industry that took us away from our fur-baby for ten hours a day and business trips that didn’t allow an extra carry-on with fur sticking out! How would we ever find someone we trusted enough to care for our baby boy? Other pet owners must be resonating with these same feelings of guilt, worry and fear.</p>
    <p>I imagined a company that could provide peace of mind for pet owners. I knew that my vision would allow others to be able to enjoy the benefits of pet ownership, while maintaining their careers, social lives and family time without holding on to the guilt. I gave up my corporate career because of this belief. I wish I could say it was the hardest thing I have ever done, but in fact it was blissfully easy, because it was meant to be. I found my path and with a lot of hard work and long hours, my vision became a reality</p>
  </div>
  <div class="about-col col-right">
    <p>Today, we are a fully-staffed company with employees (not independent contractors) who are as excited about working with pets as I am. We are continually educating ourselves and when we are not caring for pets, we are studying coursework on how to be better in-tune with dog behavior, pet health and related topics (we are a PawPath Certified business). We truly pride ourselves on giving the pets we care for a full “experience” and not just a walk. The love I have seen from my staff warms my heart and gives me hope for this world!</p>
    <p>If you have pets and experience any feelings of guilt when you need to leave them behind, reach out to us! We pick right up where you leave off, with smiles, love and adventures that can turn an ordinary day extraordinary!</p>
  </div>
  <div class="signature">
    <div class="signature-name">Dana Whitfield</div>
    <div class="signature-role">Owner, Harbor Leash LLC</div>
  </div>

  <div class="feature" style="left:20px">
    <div class="feature-art" style="background:linear-gradient(135deg,#f3c27a,#6a4a74)" role="img" aria-label="Handshake illustration"></div>
    <div class="feature-title">Vetted Employees</div>
    <p class="feature-text">We carry liability insurance, bonding and workers compensation and our staff is background checked, trained, and invested in your pet’s care.</p>
  </div>
  <div class="feature" style="left:183px">
    <div class="feature-art" style="background:linear-gradient(135deg,#7a7a72,#f2e6c8)" role="img" aria-label="Tracking screen illustration"></div>
    <div class="feature-title">Accountability</div>
    <p class="feature-text">We track our employee’s whereabouts while on the job and all management is overseen by the company’s owner.</p>
  </div>
  <div class="feature" style="left:343px">
    <div class="feature-art" style="background:linear-gradient(135deg,#f2a93a,#5D4664)" role="img" aria-label="Customer service agent illustration"></div>
    <div class="feature-title">Outstanding Customer<br>Service</div>
    <p class="feature-text">If we don’t hit it out of the park the first time, you can count on us to make it right for you.</p>
  </div>

  <div class="fold"></div>

  <div class="info-box">All of our services have an emphasis on quality care. Did you know our standard dog walking visits and pet sitting visits are untimed? This means we are not rushing in and out of your house, sacrificing care for profit. A sitter will come to your home, and spend as much time as is needed to keep your pet comfortable and happy. The minimum time spent at a dog walk is a half hour, and 45 minutes at a pet sitting visit; we also offer guaranteed one-hour visits for the days you really want to pamper your pet and tire him/her out! Let us know your needs, and we will recommend a service to match!</div>
  <div class="info-photo" style="background:linear-gradient(180deg,#8a6a70 0%,#c9a48a 45%,#5a4a48 70%,#8d7f8f 100%)" role="img" aria-label="Three dog noses peeking out from under a striped blanket"></div>

  <h2 class="services-title">Services</h2>
  <ul class="service-list">
    <li>Dog Walking</li>
    <li>Pet Sitting</li>
    <li>Cat Sitting/Small Pet Sitting</li>
    <li>Day Care &amp; Overnight Boarding</li>
    <li>Wedding Attendant</li>
  </ul>
  <span class="more">+more</span>

  <h2 class="contact-title">Contact Us</h2>
  <ul class="contact-list">
    <li><span class="contact-icon"><svg width="10" height="14" viewBox="0 0 10 14"><rect x="1" y="0.5" width="8" height="13" rx="2" fill="var(--purple)"/><rect x="2.5" y="2.5" width="5" height="6" fill="#fff"/></svg></span>201-555-0148</li>
    <li><span class="contact-icon"><svg width="16" height="12" viewBox="0 0 16 12"><rect x="0.75" y="0.75" width="14.5" height="10.5" fill="none" stroke="var(--purple)" stroke-width="1.5"/><path d="M1 1l7 6 7-6M1 11l5-5M15 11l-5-5" fill="none" stroke="var(--purple)" stroke-width="1.2"/></svg></span>info@harborleashpetcare.com</li>
    <li><span class="contact-icon"><svg width="11" height="13" viewBox="0 0 11 13"><path d="M1 0l9 7-4 .5 2.5 4.5-1.8.9L4.3 8.4 1 11z" fill="var(--purple)"/></svg></span>www.harborleashpetcare.com</li>
    <li><span class="contact-icon"><span class="dot"></span></span>/HarborLeash</li>
    <li><span class="contact-icon"><span class="dot"></span></span>/HarborLeashPets/</li>
    <li><span class="contact-icon"><span class="dot"></span></span>/HLPetCare</li>
  </ul>
</section>

</body>
</html>
```